Business Card Design for Consulting Company

I require a Business Card design for my Consulting company. <br/><br/>My company name is: Marcel Pruett Consulting Inc.<br/>My website is: www.marcelpruettconsulting.example<br/><br/>My company focuses on management and software development for the Tallyvane CRM platform (www.tallyvane.example)<br/><br/>I have a logo already designed...see attached.
Updates

Also Include my Name and Title: Marcel K.T. Pruett President

Target Market(s)

Tallyvane Customers

Contact Information for Business Card

Only include my LOGO (provided)
My Name: Marcel KT Pruett
My Title: President
My Company Name: Marcel Pruett Consulting Inc.
My Website: www.marcelpruettconsulting.example
My Email: marcel.pruett.consulting@mailbox.example

NO PHONE NUMBER
NO ADDRESS

Font styles to use
Serif
Sans Serif
Other font styles liked:
• see my website: www.marcelpruettconsulting.example

Colors

Designer to choose colors to be used in the design.

Requirements
Must have
• Must include my Orange
• Include my name (Marcel K.T. Pruett), title (President) company name, website and email
• It should also have a tag line like: Tallyvane Consulting
• I'm flexible with the tag line
Should not have
• Don't include my phone number or address

```html
<!DOCTYPE html>
<html lang="en">
<head>
<meta charset="utf-8">
<title>Marcel Pruett Consulting Inc. — Business Card</title>
<link rel="stylesheet" href="https://fonts.googleapis.com/css2?family=Jost:wght@300;400;700&display=swap">
<style>
  :root {
    --ink: #161618;
    --panel: #1a1a1c;
    --orange: #f5841f;
    --white: #ffffff;
  }
  html, body {
    margin: 0;
    padding: 0;
    width: 1200px;
    height: 777px;
    overflow: hidden;
    background: var(--ink);
  }
  .card {
    position: relative;
    width: 1200px;
    height: 777px;
    overflow: hidden;
    background: var(--ink);
    font-family: "Jost", "Futura", sans-serif;
  }
  .card__art {
    position: absolute;
    inset: 0;
  }
  .brand-name {
    position: absolute;
    left: 144px;
    width: 498px;
    top: 370px;
    margin: 0;
    text-align: center;
    color: var(--white);
    font-weight: 700;
    font-size: 25px;
    font-variant: small-caps;
    letter-spacing: 0.5px;
    line-height: 1;
  }
  .heading {
    position: absolute;
    left: 562px;
    top: 60px;
    width: 585px;
    margin: 0;
    color: var(--white);
    font-weight: 700;
    font-size: 62px;
    font-variant: small-caps;
    line-height: 1;
    white-space: nowrap;
    padding-bottom: 8px;
    border-bottom: 4px solid var(--white);
    text-align: center;
    letter-spacing: 1px;
  }
  .person {
    position: absolute;
    left: 734px;
    top: 264px;
  }
  .person__name {
    margin: 0;
    color: var(--orange);
    font-weight: 700;
    font-size: 50px;
    font-variant: small-caps;
    line-height: 1;
    white-space: nowrap;
    padding-bottom: 4px;
    border-bottom: 3px solid var(--orange);
  }
  .person__title {
    margin: 12px 0 0 -1px;
    color: var(--white);
    font-weight: 400;
    font-size: 29px;
    font-variant: small-caps;
    line-height: 1;
  }
  .contact {
    position: absolute;
    left: 700px;
    margin: 0;
    display: flex;
    align-items: center;
    gap: 11px;
    color: var(--white);
    font-weight: 700;
    font-size: 21px;
    font-variant: all-small-caps;
    letter-spacing: 0.6px;
    line-height: 1;
    white-space: nowrap;
  }
  .contact--web { top: 419px; }
  .contact--mail { top: 485px; }
  .contact__icon { flex: none; }
</style>
</head>
<body>
  <main class="card">
    <svg class="card__art" width="1200" height="777" viewBox="0 0 1200 777" aria-hidden="true">
      <defs>
        <filter id="hex-shadow" x="-20%" y="-20%" width="140%" height="140%">
          <feDropShadow dx="6" dy="6" stdDeviation="12" flood-color="#000" flood-opacity="0.6"/>
        </filter>
      </defs>
      <polygon class="accent-band" points="0,0 336,0 544,388 304,777 0,777" fill="var(--orange)"/>
      <polygon class="brand-hexagon" points="268,166 520,166 642,388 520,610 268,610 144,388" fill="var(--panel)" filter="url(#hex-shadow)"/>
    </svg>

    <p class="brand-name">Marcel Pruett Consulting Inc.</p>

    <h1 class="heading">Consulting company</h1>

    <section class="person">
      <h2 class="person__name">Marcel KT Pruett</h2>
      <p class="person__title">President</p>
    </section>

    <p class="contact contact--web">
      <svg class="contact__icon" width="24" height="24" viewBox="0 0 24 24" aria-hidden="true">
        <circle cx="12" cy="12" r="11" fill="var(--orange)"/>
        <ellipse cx="12" cy="12" rx="5" ry="11" fill="none" stroke="var(--ink)" stroke-width="1"/>
        <line x1="1" y1="12" x2="23" y2="12" stroke="var(--ink)" stroke-width="1"/>
        <line x1="3" y1="6.5" x2="21" y2="6.5" stroke="var(--ink)" stroke-width="1"/>
        <line x1="3" y1="17.5" x2="21" y2="17.5" stroke="var(--ink)" stroke-width="1"/>
      </svg>
      <span>www.marcelpruettconsulting.example</span>
    </p>

    <p class="contact contact--mail">
      <svg class="contact__icon" width="24" height="18" viewBox="0 0 24 18" aria-hidden="true">
        <rect x="0" y="1" width="24" height="16" fill="var(--orange)"/>
        <polyline points="0.5,1.5 12,10 23.5,1.5" fill="none" stroke="var(--ink)" stroke-width="1.2"/>
        <line x1="0.5" y1="16.5" x2="9" y2="8" stroke="var(--ink)" stroke-width="1"/>
        <line x1="23.5" y1="16.5" x2="15" y2="8" stroke="var(--ink)" stroke-width="1"/>
      </svg>
      <span>marcel.pruett.consulting@mailbox.example</span>
    </p>
  </main>
</body>
</html>
```